Brightmarket Tradehub (appstore) Billboards - Dealbeacon

We offer an app on the Brightmarket Tradehub - B2B app store which is called Dealbeacon. We have a presentation of our application consisting of 15 billboards with information and graphics about our application. I want a new design for our Billboards and want to have the first 5 created.

Here is our App listing and when you click on the big image you see the billboards I want to create. The first 5 is enough and I also want the template so I can create more myself.
I have added a ppt with lots of screenshots of the application

Each image/Billboard must follow these specs Specs: 700x467 pixel jpg or png no larger than 1MB

https://tradehub.brightmarket-example.com/listingDetail?listingId=k7R2B91100XQmzTPLV

Here is a video about what the Dealbeacon app does

Target Market(s)

Brightmarket customers , Sales Executives, VP Sales , Sales operations - Relevant for all industries that run a sales process based on customer meetings and/or phone meetings

Colors

Designer to choose colors to be used in the design.

Requirements
Must have
• Screenshots from the solution. The billboards is to spike interest from people viewing and also showcase how things look inside their Brightmarket solution with our Dealbeacon app running
• - SEE EXAMPLE Billboard image of what type of Billboard I am after

```html
<!DOCTYPE html>
<html lang="en">
<head>
<meta charset="utf-8">
<title>Dealbeacon Billboard – Meeting Feedback</title>
<link rel="stylesheet" href="https://fonts.googleapis.com/css2?family=Lexend:wght@300;400;600&family=Open+Sans:wght@400;600&display=swap">
<style>
  :root {
    --navy: #06055f;
    --navy-wave: #16157a;
    --yellow: #ffff00;
    --orange: #ff6a10;
    --white: #ffffff;
    --ui-line: #d8dbe2;
    --ui-text: #3d4350;
    --ui-muted: #8a909c;
    --ui-blue: #1f8ef1;
    --chip: #7d6be0;
  }
  * { box-sizing: border-box; margin: 0; padding: 0; }
  html, body { width: 1200px; height: 1200px; overflow: hidden; background: var(--white); }
  .billboard {
    position: absolute; left: 222px; top: 347px; width: 756px; height: 507px;
    background: var(--navy); overflow: hidden; border: 1px solid #222;
    font-family: "Lexend", sans-serif;
  }
  .billboard__shapes { position: absolute; inset: 0; }
  .headline {
    position: absolute; left: 26px; top: 48px; width: 340px;
    color: var(--yellow); font-weight: 600; font-size: 29.5px; line-height: 31.6px;
    letter-spacing: -0.2px;
  }
  .benefits {
    position: absolute; left: 29px; top: 245px; width: 303px;
    list-style: none; color: var(--white); font-weight: 300;
    font-size: 17.2px; line-height: 21.8px;
  }
  .benefits li { position: relative; padding-left: 27px; text-align: justify; text-align-last: left; }
  .benefits li::before {
    content: ""; position: absolute; left: 0; top: 10px; width: 4px; height: 4px;
    border-radius: 50%; background: var(--white);
  }
  .callout { position: absolute; left: 27px; top: 400px; }
  .callout__line {
    display: block; width: max-content; background: var(--orange); color: var(--white);
    font-weight: 600; font-size: 21.5px; line-height: 30px; padding: 0 6px 0 8px;
    margin-bottom: 6px; letter-spacing: -0.2px;
  }
  /* in-app screenshot */
  .app-ui { position: absolute; left: 370px; top: 25px; width: 386px; height: 260px; font-family: "Open Sans", sans-serif; color: var(--ui-text); }
  .app-ui__url {
    position: absolute; left: 104px; top: 4px; width: 258px; height: 12px;
    border: 1px solid var(--ui-line); font-size: 6px; line-height: 10px; padding-left: 3px; color: var(--ui-muted);
    white-space: nowrap; overflow: hidden;
  }
  .app-ui__topbar { position: absolute; left: 104px; top: 18px; width: 282px; height: 38px; background: #f3f4f6; border-bottom: 1px solid var(--ui-line); }
  .app-ui__form { position: absolute; left: 0; top: 72px; width: 369px; height: 85px; border: 1px solid var(--ui-line); border-radius: 2px; background: var(--white); }
  .app-ui__label { position: absolute; left: 5px; font-size: 5.5px; color: var(--ui-muted); }
  .app-ui__chips { position: absolute; left: 6px; top: 21px; display: flex; gap: 5px; }
  .chip { font-size: 6.5px; line-height: 10px; padding: 0 3px; border: 1px solid var(--ui-line); border-radius: 2px; display: flex; align-items: center; gap: 3px; }
  .chip__icon { width: 8px; height: 6px; background: var(--chip); border-radius: 1px; }
  .app-ui__search { position: absolute; left: 5px; top: 34px; width: 356px; height: 13px; border: 1px solid var(--ui-line); border-radius: 2px; font-size: 6px; line-height: 11px; padding-left: 6px; color: var(--ui-muted); }
  .app-ui__select { position: absolute; left: 5px; top: 63px; width: 356px; height: 15px; border: 1px solid var(--ui-blue); border-radius: 2px; font-size: 6.5px; line-height: 13px; padding-left: 5px; }
  .app-ui__options { position: absolute; left: 7px; top: 153px; width: 355px; list-style: none; border-left: 1px solid var(--ui-line); border-bottom: 1px solid var(--ui-line); background: var(--white); padding-top: 1px; }
  .app-ui__options li { font-size: 6.2px; line-height: 8.8px; padding-left: 4px; }
  .app-ui__options .is-selected { background: var(--ui-blue); color: var(--white); }
  .app-ui__scroll { position: absolute; left: 362px; top: 192px; width: 8px; height: 15px; background: var(--ui-blue); border-radius: 1px; }
  .brand { position: absolute; left: 525px; top: 306px; width: 198px; }
  .brand__row { display: flex; align-items: center; justify-content: flex-end; gap: 7px; }
  .brand__mark { width: 34px; height: 34px; border-radius: 50%; background: var(--orange); }
  .brand__name { color: var(--orange); font-weight: 600; font-size: 29px; line-height: 36px; letter-spacing: -0.3px; }
  .brand__tagline { color: var(--orange); font-weight: 600; font-size: 7px; text-align: right; margin-top: 1px; }
</style>
</head>
<body>
<section class="billboard">
  <svg class="billboard__shapes" viewBox="0 0 756 507" width="756" height="507" aria-hidden="true">
    <path fill="var(--navy-wave)" d="M470 3 H756 V430 C690 440 620 420 575 405 C500 378 390 370 360 330 C330 290 350 250 300 215 C270 190 270 160 300 130 C330 100 390 70 430 40 C450 20 460 8 470 3 Z"/>
    <path fill="var(--white)" d="M514 3 H756 V401 C690 405 620 395 594 377 C560 355 440 355 410 341 C370 325 368 290 386 248 C395 220 330 210 303 190 C285 175 285 150 306 165 C280 140 320 110 362 101 C405 92 440 75 458 53 C480 25 495 8 514 3 Z"/>
  </svg>

  <h1 class="headline">Analyze Prospects Reactions and Sentiments Immediately After Your Meetings</h1>

  <ul class="benefits">
    <li>Request feedback based on what kind of meeting you had with the customer</li>
    <li>Ask different questions at different stages of your sales cycle</li>
  </ul>

  <div class="app-ui">
    <div class="app-ui__topbar"></div>
    <div class="app-ui__url">…db_requestFeedbackDeal?viewCache=1&amp;id=0071200000KXmrT</div>
    <div class="app-ui__form">
      <span class="app-ui__label" style="top:9px">Recipients</span>
      <div class="app-ui__chips">
        <span class="chip"><span class="chip__icon"></span>Nora Whitt ✕</span>
        <span class="chip"><span class="chip__icon"></span>Leon Marsh ✕</span>
      </div>
      <div class="app-ui__search">Search</div>
      <span class="app-ui__label" style="top:52px">Survey Form</span>
      <div class="app-ui__select">01 · Introduction meeting</div>
    </div>
    <ul class="app-ui__options">
      <li>Select a Survey</li>
      <li>01 · Introduction meeting</li>
      <li>02 · Discovery meeting</li>
      <li class="is-selected">03 · Demo meeting</li>
      <li>04 · WS evaluation</li>
      <li>05 · Negotiations</li>
      <li>06 · Client Feedback</li>
      <li>07 · Project delivery</li>
      <li>08 · Customer Satisfaction (CSAT)</li>
      <li>09 · Advisory &amp; Analyst Call Feedback</li>
      <li>10 · Informal meeting</li>
    </ul>
    <div class="app-ui__scroll"></div>
  </div>

  <div class="brand">
    <div class="brand__row"><span class="brand__mark"></span><span class="brand__name">Dealbeacon</span></div>
    <div class="brand__tagline">A Northwave Company</div>
  </div>

  <div class="callout">
    <span class="callout__line">DETECT MISSING INFORMATION AND</span>
    <span class="callout__line">MISUNDERSTANDINGSAND ADRESS THEM IMMEDIATELY</span>
  </div>
</section>
</body>
</html>
```